Weight Loss Banner Ad

We need banner ads for our website, www.brightplatekitchen.com. We would like to see Banner ads that represent what you think is the most captivating aspect of The MealWise Plan. Please review the website.

The banner ad should be something you REALLY want to click on. It needs to include the name and/or logo and the slogan "Gourmet Meals Direct To Your House"

We will want the final ad in multiple sizes but it should use the same image and copy.

Logo is attached, so are images. Feel free to use your own if you think you have a better on

Size (pixels):
468 x 60
392 x 72
234 x 60
125 x 125
120 x 90
120 x 60
88 x 31
120 x 240
120 x 600
160 x 600

Target Market(s)

Fitness Enthusiast looking to lose weight.

Industry/Entity Type

Weight

Font styles to use
Sans Serif

Requirements
Must have
• See Description
Nice to have
• Should be awesome and make you want to buy some food. Also you may want to say something about the price:

i.e. Starting at only $99

```html
<!DOCTYPE html>
<html lang="en">
<head>
<meta charset="utf-8">
<title>The MealWise Plan – Banner</title>
<link rel="stylesheet" href="https://fonts.googleapis.com/css2?family=Arimo:wght@400&display=swap">
<style>
  :root {
    --sky-blue: #8fcbe0;
    --sky-pale: #d8eef0;
    --sun-cream: #fbf6d6;
    --haze-white: #fffbe8;
    --field-green: #8fb45a;
    --tree-green: #4f7a36;
    --earth-brown: #8a6a4c;
    --skin-tone: #e2a77c;
    --headline-white: #ffffff;
  }
  html, body {
    margin: 0;
    padding: 0;
    width: 1200px;
    height: 1015px;
    overflow: hidden;
    background: var(--haze-white);
  }
  .banner {
    position: relative;
    width: 1200px;
    height: 1015px;
    overflow: hidden;
  }
  .hero-photo {
    position: absolute;
    inset: 0;
    background:
      radial-gradient(ellipse 520px 420px at 900px 300px, var(--haze-white) 0%, rgba(255,251,232,0) 75%),
      radial-gradient(ellipse 360px 520px at 470px 520px, rgba(226,167,124,0.55) 0%, rgba(226,167,124,0) 70%),
      linear-gradient(160deg, rgba(79,122,54,0) 62%, var(--field-green) 80%, var(--tree-green) 92%, var(--earth-brown) 100%),
      linear-gradient(120deg, var(--sky-blue) 0%, var(--sky-pale) 38%, var(--sun-cream) 70%, var(--haze-white) 100%);
  }
  .brand-name {
    position: absolute;
    left: 0;
    top: 480px;
    width: 980px;
    margin: 0;
    font-family: "Arimo", Arial, sans-serif;
    font-weight: 400;
    color: var(--headline-white);
    text-align: center;
    text-transform: uppercase;
    letter-spacing: -2px;
  }
  .brand-name span {
    display: block;
  }
  .brand-name .line-one {
    font-size: 186px;
    line-height: 210px;
  }
  .brand-name .line-two {
    font-size: 214px;
    line-height: 210px;
  }
  .slogan {
    position: absolute;
    left: 0;
    top: 915px;
    width: 980px;
    margin: 0;
    font-family: "Arimo", Arial, sans-serif;
    font-weight: 400;
    font-size: 44px;
    line-height: 56px;
    color: var(--headline-white);
    text-align: center;
    letter-spacing: 0.5px;
  }
</style>
</head>
<body>
  <main class="banner">
    <div class="hero-photo" role="img" aria-label="Photo of a woman in running shorts and sneakers sprinting across a grassy hill under a bright, sunlit sky"></div>
    <h1 class="brand-name">
      <span class="line-one">MealWise</span>
      <span class="line-two">Plan</span>
    </h1>
    <p class="slogan">Gourmet Meals Direct To Your House</p>
  </main>
</body>
</html>
```